Frostwell Supply - Liquid Nitrogen Business Flyer

I would like a flyer for a direct mailing campaign. The target audience is strictly professional (doctors) and will be mailed to their place of business.
My company (Frostwell Supply) sells and delivers medical liquid nitrogen along with renting accessories that has to do with liquid nitrogen.

The main company is Frostwell Supply; however, Polarvane Holdings (one of the logos are attached) is its parent company and I would like it included in a small way. Around Polarvane Holdings logo - ESTABLISHED 1963

Components of the flyer:

FIRST FILL FREE

Prices are flat rate (no hidden fees... hazmat, delivery, etc.)

-Guarantee -
Will beat any competitor’s price

------Route based services ------
Set-up once and we do the rest
Peace of mind knowing you will have product

----Equipment Rentals----
Dewars-Stands-Cryoguns-Withdrawal Systems

Include ------
Company Name

(555) 382-7164

email address

Some things can be re-worded or left off, your option.. You can ask me questions anytime if any questions arise. If you come up with a "slogan” and use it on the flyer, feel free

Thank you.

Target Market(s)

Dermatologist and Family Doctors

Industry/Entity Type

Business

Colors
f37122
add136
e34297
0255a3

Requirements
Must have
• Catch the mangers eye and relay a positive message very quickly
• Be bright, colorful and CLASSY
• Have 2 sides
• Catchy and smart and abstract WILL win
Nice to have
• The flyer needs to be editable to plug in my information and any changes that might come. I work on Corel Draw X6 for editing.
• 3.74" x 8.27" LONG

```html
<!DOCTYPE html>
<html lang="en">
<head>
<meta charset="utf-8">
<title>Frostwell Supply – Liquid Nitrogen Flyer</title>
<link href="https://fonts.googleapis.com/css2?family=Source+Sans+3:wght@400;600;700&display=swap" rel="stylesheet">
<style>
  :root{
    --orange:#f37122;
    --orange-light:#f79a4e;
    --lime:#add136;
    --lime-soft:#b5d86a;
    --pink:#e34297;
    --blue:#0255a3;
    --ink:#2b2b2b;
    --paper:#ffffff;
    --stage:#e6e7ea;
  }
  *{box-sizing:border-box;margin:0;padding:0}
  html,body{width:900px;height:1200px;overflow:hidden}
  body{
    background:var(--stage);
    font-family:"Source Sans 3",Arial,sans-serif;
    display:flex;align-items:center;justify-content:center;
  }
  .flyer{
    position:relative;width:520px;height:1150px;
    background:var(--paper);overflow:hidden;
    box-shadow:0 6px 24px rgba(0,0,0,.18);
  }
  .flyer__shapes{position:absolute;inset:0;width:100%;height:100%}
  .brand{
    position:absolute;top:38px;left:0;width:100%;
    text-align:center;color:var(--blue);
    font-weight:700;font-size:38px;letter-spacing:.5px;
  }
  .hero-illustration{
    position:absolute;left:170px;top:175px;width:300px;height:290px;
    border-radius:50% 40% 45% 55%;
    background:radial-gradient(circle at 55% 45%,#e86aa9 0%,rgba(227,66,151,.55) 45%,rgba(243,113,34,0) 72%);
  }
  .ribbon{
    position:absolute;left:0;top:318px;height:44px;width:300px;
    background:var(--blue);color:#fff;
    border-top:3px solid #fff;border-bottom:3px solid #fff;border-right:3px solid #fff;
    border-radius:0 8px 8px 0;
    font-weight:600;font-size:27px;letter-spacing:1px;
    display:flex;align-items:center;padding-left:26px;
  }
  .pricing{
    position:absolute;left:28px;top:378px;width:440px;
    color:#fff;font-size:33px;line-height:1.12;font-weight:400;
  }
  .services{
    position:absolute;left:28px;top:588px;width:440px;height:282px;
    background:var(--lime-soft);border-radius:18px;
    padding:22px 24px;
    display:flex;flex-direction:column;gap:20px;
    color:var(--ink);font-size:21px;line-height:1.18;
  }
  .services__label{color:var(--pink);font-weight:700;font-size:25px}
  .van-illustration{
    position:absolute;left:265px;top:930px;width:240px;height:180px;
    border-radius:20px;
    background:linear-gradient(160deg,#f4f6f9 0%,#dfe5ee 100%);
  }
  .parent-brand{
    position:absolute;left:28px;top:1040px;
    display:flex;align-items:center;gap:8px;
    color:var(--blue);font-weight:700;font-size:17px;
  }
  .parent-brand__dot{width:22px;height:22px;border-radius:50%;background:var(--lime)}
  .phone{
    position:absolute;left:28px;top:1098px;
    color:var(--blue);font-weight:600;font-size:24px;
  }
</style>
</head>
<body>
  <article class="flyer">
    <svg class="flyer__shapes" viewBox="0 0 520 1150" preserveAspectRatio="none" aria-hidden="true">
      <defs>
        <linearGradient id="panelGradient" x1="0" y1="0" x2="1" y2="1">
          <stop offset="0" stop-color="#f79a4e"/>
          <stop offset=".5" stop-color="#f37122"/>
          <stop offset="1" stop-color="#f0801f"/>
        </linearGradient>
      </defs>
      <!-- top bands -->
      <path d="M0 175 C160 150 340 118 520 96 L520 118 C340 140 160 172 0 200 Z" fill="#add136"/>
      <path d="M0 196 C160 168 340 136 520 114 L520 150 C340 170 160 198 0 230 Z" fill="#0255a3"/>
      <!-- orange panel -->
      <path d="M0 226 C160 194 340 166 520 146 L520 890 C360 900 170 940 0 990 Z" fill="url(#panelGradient)"/>
      <!-- bottom bands -->
      <path d="M0 986 C170 936 360 896 520 886 L520 914 C360 922 170 962 0 1014 Z" fill="#0255a3"/>
      <path d="M0 1014 C170 962 360 922 520 914 L520 924 C360 934 170 974 0 1026 Z" fill="#add136"/>
    </svg>

    <h1 class="brand">Frostwell Supply</h1>

    <div class="hero-illustration" role="img" aria-label="Illustration of a delivery worker walking while carrying a box"></div>

    <div class="ribbon">FIRST FILL FREE</div>

    <p class="pricing">Prices are flat rate (no hidden fees... hazmat, delivery, etc.)</p>

    <section class="services">
      <p><span class="services__label">Guarantee</span> - Will beat any competitor’s price</p>
      <p><span class="services__label">Route based services -</span><br>Set-up once and we do the rest Peace of mind knowing you will have product</p>
      <p><span class="services__label">Equipment Rentals</span> - Dewars-Stands-Cryoguns-Withdrawal Systems</p>
    </section>

    <div class="van-illustration" role="img" aria-label="Line drawing of a delivery van"></div>

    <div class="parent-brand"><span class="parent-brand__dot"></span>Polarvane Holdings</div>
    <p class="phone">(555) 382-7164</p>
  </article>
</body>
</html>
```